Business card for new consulting business - Brenvale Holdings Pty Ltd.

Consulting in the areas of Occupational Health, Safety and Community Relations in the resources (mining) industries. The consultant (me) will work both within Australia and overseas jurisdictions such as South East Asia, Africa , South America etc, often working with third world indigenous communities. The design should suggest a high level of social and environmental responsibility.

```html
<!DOCTYPE html>
<html lang="en">
<head>
<meta charset="utf-8">
<title>Brenvale Holdings Pty Ltd — Stationery</title>
<link rel="stylesheet" href="https://fonts.googleapis.com/css2?family=Montserrat:wght@500;600&display=swap">
<style>
  :root {
    --green: #3bb54a;
    --grey: #58585a;
    --ink-dark: #03040f;
    --paper: #ffffff;
  }
  * { box-sizing: border-box; margin: 0; padding: 0; }
  html, body { width: 1200px; height: 1200px; overflow: hidden; }
  body { font-family: "Montserrat", Arial, sans-serif; background: var(--paper); position: relative; }

  .brand-stage { position: absolute; left: 0; top: 0; width: 1200px; height: 454px; display: flex; align-items: center; justify-content: center; }
  .lockup { display: flex; align-items: center; gap: 18px; color: var(--green); font-weight: 600; }
  .lockup .dot { width: 96px; height: 96px; border-radius: 50%; background: var(--green); flex: none; }
  .lockup .name { line-height: 1.05; }
  .lockup .name .main { display: block; font-size: 64px; letter-spacing: 1px; }
  .lockup .name .sub { display: block; font-size: 30px; letter-spacing: 3px; }

  .stationery-stage { position: absolute; left: 0; top: 454px; width: 1200px; height: 746px; background: var(--ink-dark); }

  .letterhead { position: absolute; left: 70px; top: 46px; width: 450px; height: 650px; background: var(--paper); overflow: hidden; }
  .letterhead .top-band { position: absolute; left: 0; top: 0; width: 100%; height: 46px; background: var(--green); }
  .letterhead .mini-brand { position: absolute; left: 0; right: 0; top: 66px; display: flex; justify-content: center; align-items: center; gap: 8px; color: var(--green); font-weight: 600; }
  .mini-brand .dot { width: 24px; height: 24px; border-radius: 50%; background: var(--green); flex: none; }
  .mini-brand .label { font-size: 17px; line-height: 1.05; white-space: nowrap; }
  .mini-brand .label small { display: block; font-size: 9px; letter-spacing: 1px; }
  .letterhead .sender { position: absolute; left: 140px; bottom: 76px; font-size: 12px; font-weight: 600; color: var(--green); white-space: nowrap; }
  .letterhead .contacts { position: absolute; right: 24px; bottom: 74px; }
  .letterhead .bottom-band { position: absolute; left: 0; bottom: 0; width: 100%; height: 52px; background: var(--grey); color: var(--paper); font-size: 10px; letter-spacing: 2.5px; display: flex; align-items: center; justify-content: center; }

  .contacts { display: grid; grid-template-columns: max-content max-content; column-gap: 12px; row-gap: 3px; color: var(--green); font-size: 7px; white-space: nowrap; }
  .contacts .row { display: flex; align-items: center; gap: 5px; white-space: nowrap; }
  .contacts svg { width: 8px; height: 8px; fill: var(--green); flex: none; }

  .card { position: absolute; width: 440px; height: 258px; overflow: hidden; }
  .card-front { left: 640px; top: 46px; background: var(--paper); }
  .card-front .top-band { position: absolute; left: 0; top: 0; width: 100%; height: 38px; background: var(--green); }
  .card-front .mini-brand { position: absolute; left: 0; right: 0; top: 78px; display: flex; justify-content: center; align-items: center; gap: 10px; color: var(--green); font-weight: 600; }
  .card-front .mini-brand .dot { width: 44px; height: 44px; }
  .card-front .mini-brand .label { font-size: 28px; }
  .card-front .mini-brand .label small { font-size: 12px; letter-spacing: 1.5px; }
  .card-front .holder { position: absolute; left: 49px; top: 164px; font-size: 16px; font-weight: 500; color: var(--green); white-space: nowrap; }
  .card-front .contacts { position: absolute; right: 40px; top: 164px; font-size: 9px; row-gap: 5px; column-gap: 12px; }
  .card-front .contacts svg { width: 9px; height: 9px; }
  .card-front .bottom-band { position: absolute; left: 0; bottom: 0; width: 100%; height: 38px; background: var(--grey); color: var(--paper); font-size: 12px; font-weight: 600; letter-spacing: 3px; display: flex; align-items: center; justify-content: center; }

  .card-back { left: 640px; top: 400px; background: var(--grey); display: flex; align-items: center; justify-content: center; }
  .card-back .mini-brand { display: flex; align-items: center; gap: 12px; color: var(--paper); font-weight: 600; }
  .card-back .dot { width: 56px; height: 56px; border-radius: 50%; background: var(--paper); }
  .card-back .label { font-size: 34px; line-height: 1.05; }
  .card-back .label small { display: block; font-size: 14px; letter-spacing: 1.5px; }
</style>
</head>
<body>
  <svg width="0" height="0" style="position:absolute" aria-hidden="true">
    <symbol id="icon-phone" viewBox="0 0 10 10"><path d="M2 0.5 L3.6 2.6 L2.8 3.6 Q4 5.8 6.4 7.2 L7.4 6.4 L9.5 8 L8.4 9.5 Q3.8 9 0.5 1.6 Z"/></symbol>
    <symbol id="icon-mobile" viewBox="0 0 10 10"><path d="M2.5 0 H7.5 V10 H2.5 Z M3.5 1 V8 H6.5 V1 Z"/></symbol>
    <symbol id="icon-fax" viewBox="0 0 10 10"><path d="M2.5 0 H7.5 V3 H2.5 Z M0.5 3.5 H9.5 V7.5 H8 V6 H2 V7.5 H0.5 Z M2.5 6.5 H7.5 V10 H2.5 Z"/></symbol>
    <symbol id="icon-mail" viewBox="0 0 10 10"><path d="M0.5 2 H9.5 L5 5.5 Z M0.5 3 L5 6.5 L9.5 3 V8 H0.5 Z"/></symbol>
  </svg>

  <section class="brand-stage">
    <div class="lockup">
      <span class="dot"></span>
      <span class="name"><span class="main">Brenvale</span><span class="sub">Holdings Pty Ltd.</span></span>
    </div>
  </section>

  <section class="stationery-stage">
    <article class="letterhead">
      <div class="top-band"></div>
      <div class="mini-brand">
        <span class="dot"></span>
        <span class="label">Brenvale<small>Holdings Pty Ltd.</small></span>
      </div>
      <p class="sender">YOUR NAME</p>
      <div class="contacts">
        <span class="row"><svg><use href="#icon-phone"/></svg>000-000-0000</span>
        <span class="row"><svg><use href="#icon-fax"/></svg>000-000-0000</span>
        <span class="row"><svg><use href="#icon-mobile"/></svg>000-000-0000</span>
        <span class="row"><svg><use href="#icon-mail"/></svg>info@brenvale.example</span>
      </div>
      <div class="bottom-band">www.brenvale.example</div>
    </article>

    <article class="card card-front">
      <div class="top-band"></div>
      <div class="mini-brand">
        <span class="dot"></span>
        <span class="label">Brenvale<small>Holdings Pty Ltd.</small></span>
      </div>
      <p class="holder">YOUR NAME</p>
      <div class="contacts">
        <span class="row"><svg><use href="#icon-phone"/></svg>000-000-0000</span>
        <span class="row"><svg><use href="#icon-fax"/></svg>000-000-0000</span>
        <span class="row"><svg><use href="#icon-mobile"/></svg>000-000-0000</span>
        <span class="row"><svg><use href="#icon-mail"/></svg>info@brenvale.example</span>
      </div>
      <div class="bottom-band">www.brenvale.example</div>
    </article>

    <article class="card card-back">
      <div class="mini-brand">
        <span class="dot"></span>
        <span class="label">Brenvale<small>Holdings Pty Ltd.</small></span>
      </div>
    </article>
  </section>
</body>
</html>
```